Cover for Inspirational Daily Journal

This is the cover for a daily journal that will focus on inspirational content for black women. The cover should have a picture or silhouette of a black woman with a crown. The title is: "Grace in Bloom: A Year of Bright Mornings." The back won't have any words. Also the journal will be published on Pagewick.

```html
<!DOCTYPE html>
<html lang="en">
<head>
<meta charset="utf-8">
<title>Grace in Bloom – Journal Cover</title>
<link rel="stylesheet" href="https://fonts.googleapis.com/css2?family=Cormorant+Garamond:wght@500;600;700&display=swap">
<style>
  :root {
    --page-bg: #ffffff;
    --cover-dark: #2c150e;
    --cover-mid: #7a3a1e;
    --cover-glow: #c9662f;
    --figure-dark: #140b08;
    --figure-edge: #2a140c;
    --title-light: #f4eee8;
    --title-accent: #e3893d;
    --back-black: #1b1b1b;
    --panel-shadow: rgba(0, 0, 0, 0.12);
  }
  * { margin: 0; padding: 0; box-sizing: border-box; }
  html, body {
    width: 1200px;
    height: 655px;
    overflow: hidden;
    background: var(--page-bg);
  }
  .spread {
    position: relative;
    width: 1200px;
    height: 655px;
  }
  .front-cover,
  .back-cover {
    position: absolute;
    top: 15px;
    width: 444px;
    height: 623px;
    box-shadow: 0 1px 4px var(--panel-shadow);
    overflow: hidden;
  }
  .front-cover { left: 141px; }
  .back-cover {
    left: 614px;
    background: var(--back-black);
  }
  .cover-art {
    position: absolute;
    inset: 0;
    background:
      radial-gradient(ellipse 75% 60% at 70% 70%, var(--cover-glow) 0%, var(--cover-mid) 55%, var(--cover-dark) 100%);
  }
  .figure-placeholder {
    position: absolute;
    left: 30px;
    top: 22px;
    width: 335px;
    bottom: 0;
    border-radius: 170px 170px 30px 30px / 230px 230px 0 0;
    background: radial-gradient(ellipse 80% 70% at 50% 45%, var(--figure-dark) 60%, var(--figure-edge) 100%);
    box-shadow: 0 0 24px 6px rgba(20, 11, 8, 0.55);
  }
  .cover-title {
    position: absolute;
    left: 0;
    right: 0;
    top: 120px;
    text-align: center;
    font-family: "Cormorant Garamond", Georgia, serif;
    text-transform: uppercase;
    color: var(--title-light);
  }
  .title-lead {
    display: block;
    font-size: 28px;
    font-weight: 600;
    letter-spacing: 0.5px;
    line-height: 1;
  }
  .title-main {
    display: block;
    margin-top: 2px;
    font-size: 72px;
    font-weight: 600;
    line-height: 0.92;
    color: var(--title-accent);
  }
  .title-sub {
    display: block;
    margin-top: 4px;
    font-size: 25px;
    font-weight: 600;
    letter-spacing: 0.2px;
    line-height: 1;
  }
  .cover-label {
    position: absolute;
    left: 0;
    right: 0;
    top: 582px;
    text-align: center;
    font-family: "Cormorant Garamond", Georgia, serif;
    font-size: 15px;
    font-weight: 700;
    text-transform: uppercase;
    color: var(--title-light);
  }
</style>
</head>
<body>
  <main class="spread">
    <section class="front-cover">
      <div class="cover-art"></div>
      <div class="figure-placeholder" role="img" aria-label="Silhouette in profile of a Black woman wearing an ornate crown and a hoop earring, set against a warm orange-brown glow"></div>
      <h1 class="cover-title">
        <span class="title-lead">Grace in</span>
        <span class="title-main">Bloom</span>
        <span class="title-sub">A Year of Bright Mornings</span>
      </h1>
      <p class="cover-label">Daily Journal</p>
    </section>
    <section class="back-cover" aria-label="Back cover"></section>
  </main>
</body>
</html>
```